Business cards, envelopes, etc. for real estate company

We have a finished logo for our real estate company. We need a corporate identity package with the following items:

1. Business Cards
2. Letterhead/Stationary - with 2 pages:
-1st page with full header
-2nd page without top header
3. Concise and professional e-mail signature image
4. Fax coversheet
5. Shipping label, with our return address and a mail-to address (on one label)

We need these to be editable. We don't know the industry standard for these items but perhaps you can provide them to us in .PDF and Word format (and if you use Adobe Illustrator for them, .AI as well).

Please use the attached placeholder logo in your design entry. We will provide you with the original logo to swap in (same size and design, just different text) when we choose your entry.

Please include the following information on the letterhead and business cards:

58 Birchwell Road
Suite 2B West
New York, NY 10587

Tel: 555-014-2837
Fax :555-014-2837

Please contact us if you have any questions about this contest.

Hi,

Thanks for your interest in this project. The logo to use should be working now. Please contact me if you have any further issues or questions.

I look forward to seeing your submissions. 

Hi,

We first wish to thank you all for your submissions. 

Here is some general feedback regarding the designs shown:

1. We would prefer square (as opposed to rounded) business cards.

2. For the fax coversheets, we are looking with a designed look. While we understand these are samples, we don't want it to appear as if it a standard block of text or a fax template from a word processing program.

3. For the 1st page of letterhead and envelopes, we do need an office address on them. The envelopes should have space for a stamp in the top right corner. We would prefer the envelopes not to have colored stripes.

4. We think a watermark of the logo is an interesting idea on the business cards and/or letterhead. This may be something to try. However, it is not strictly necessary and we would like to evaluate designs with and without it.

In general we are looking for a clean yet professional look.

We are actively reviewing all entries and thank you for your time and creativity.

One last comment: We understand making all objects in the brief takes some time. However, we want to remind all the designers that this contest is for more than just business cards (envelopes, letterheads, etc.) so if we choose your design, those items will be expected. Please refer to the original brief to see what we are requesting.

If you provide a mockup of any item listed in the brief (in addition to business cards) it would help us visualize your entire vision for this project.

```html
<!DOCTYPE html>
<html lang="en">
<head>
<meta charset="utf-8">
<title>Harrow &amp; Vale — Stationery Set</title>
<link rel="stylesheet" href="https://fonts.googleapis.com/css2?family=Questrial&family=Montserrat:wght@400;600&display=swap">
<style>
  :root {
    --navy: #1f3f5e;
    --navy-deep: #1b3654;
    --navy-light: #3a6f9f;
    --paper: #ffffff;
    --backdrop: #e3e3e3;
    --grey-text: #7b7f83;
    --card-text: #dfe7ef;
  }
  * { margin: 0; padding: 0; box-sizing: border-box; }
  html, body { width: 1200px; height: 853px; overflow: hidden; }
  body {
    background: var(--backdrop);
    position: relative;
    font-family: "Montserrat", Arial, sans-serif;
  }
  .card {
    position: absolute;
    width: 340px;
    height: 196px;
    box-shadow: 0 6px 14px rgba(0,0,0,0.18);
  }
  .card--blue {
    background: radial-gradient(circle at 10% 0%, var(--navy-light) 0%, var(--navy) 55%, var(--navy-deep) 100%);
    color: var(--card-text);
  }
  .card--white { background: var(--paper); color: var(--grey-text); }
  .card--left { left: 50px; top: 60px; }
  .card--center { left: 430px; top: 60px; }
  .card--right { left: 810px; top: 60px; }

  .wordmark {
    position: absolute;
    display: flex;
    align-items: center;
    gap: 10px;
  }
  .wordmark__square { width: 34px; height: 34px; flex: none; }
  .wordmark__name {
    font-family: "Questrial", Arial, sans-serif;
    font-size: 21px;
    line-height: 1.0;
  }
  .card--blue .wordmark__square { background: var(--card-text); }
  .card--blue .wordmark__name { color: var(--card-text); }
  .card--white .wordmark__square { background: var(--navy); }
  .card--white .wordmark__name { color: var(--grey-text); }

  .card__address {
    position: absolute;
    font-size: 8.5px;
    line-height: 1.35;
    text-align: right;
  }
  .card__address b { font-weight: 600; }
  .card__person { position: absolute; }
  .card__name { font-size: 10px; font-weight: 600; letter-spacing: 0.3px; }
  .card__title { font-size: 8px; }

  .card--blue .wordmark { left: 160px; top: 44px; }
  .card--blue .card__address { left: 30px; top: 42px; width: 120px; }
  .card--blue .card__person { left: 40px; top: 140px; }

  .card--white .wordmark { left: 30px; top: 40px; }
  .card--white .card__person { right: 30px; top: 60px; text-align: right; }
  .card--white .card__name { color: var(--navy); }
  .card--white .card__address { right: 30px; top: 130px; text-align: right; }

  .envelope {
    position: absolute;
    left: 140px;
    top: 320px;
    width: 920px;
    height: 440px;
    background: var(--paper);
    box-shadow: 0 8px 18px rgba(0,0,0,0.16);
    overflow: hidden;
  }
  .envelope__flap { position: absolute; left: 0; top: 0; width: 920px; height: 70px; }
  .envelope .wordmark { left: 60px; bottom: 60px; gap: 16px; }
  .envelope .wordmark__square { width: 70px; height: 70px; background: var(--navy); }
  .envelope .wordmark__name { font-size: 40px; color: var(--grey-text); }
  .envelope__contact {
    position: absolute;
    right: 60px;
    top: 120px;
    display: flex;
    gap: 26px;
    font-size: 14px;
    line-height: 1.5;
    color: var(--grey-text);
  }
  .envelope__address { text-align: right; }
  .envelope__phones b { color: var(--navy); font-weight: 600; }
</style>
</head>
<body>

  <section class="card card--blue card--left" aria-label="Business card front">
    <div class="card__address">
      58 Birchwell Road<br>
      Suite 2B West<br>
      New York, NY 10587<br>
      <b>Phone:</b> 555-014-2837<br>
      <b>Fax:</b> 555-014-2838
    </div>
    <div class="wordmark">
      <span class="wordmark__square"></span>
      <span class="wordmark__name">Harrow<br>&amp; Vale</span>
    </div>
    <div class="card__person">
      <div class="card__name">DANIEL REYES</div>
      <div class="card__title">Managing Director</div>
    </div>
  </section>

  <section class="card card--white card--center" aria-label="Business card back">
    <div class="wordmark">
      <span class="wordmark__square"></span>
      <span class="wordmark__name">Harrow<br>&amp; Vale</span>
    </div>
    <div class="card__person">
      <div class="card__name">DANIEL REYES</div>
      <div class="card__title">Managing Director</div>
    </div>
    <div class="card__address">
      58 Birchwell Road, Suite 2B West, New York, NY 10587<br>
      <b>Phone:</b> 555-014-2837 &nbsp;<b>Fax:</b> 555-014-2838
    </div>
  </section>

  <section class="card card--blue card--right" aria-label="Business card front">
    <div class="card__address">
      58 Birchwell Road<br>
      Suite 2B West<br>
      New York, NY 10587<br>
      <b>Phone:</b> 555-014-2837<br>
      <b>Fax:</b> 555-014-2838
    </div>
    <div class="wordmark">
      <span class="wordmark__square"></span>
      <span class="wordmark__name">Harrow<br>&amp; Vale</span>
    </div>
    <div class="card__person">
      <div class="card__name">DANIEL REYES</div>
      <div class="card__title">Managing Director</div>
    </div>
  </section>

  <section class="envelope" aria-label="Envelope">
    <svg class="envelope__flap" viewBox="0 0 920 70" preserveAspectRatio="none" aria-hidden="true">
      <path d="M0 0 H920 V20 Q920 40 900 42 L40 62 Q0 64 0 40 Z" fill="var(--navy)"/>
    </svg>
    <div class="envelope__contact">
      <div class="envelope__address">
        58 Birchwell Road, Suite 2B West<br>
        New York, NY 10587
      </div>
      <div class="envelope__phones">
        <b>Tel:</b> 555-014-2837<br>
        <b>Fax:</b> 555-014-2838
      </div>
    </div>
    <div class="wordmark">
      <span class="wordmark__square"></span>
      <span class="wordmark__name">Harrow<br>&amp; Vale</span>
    </div>
  </section>

</body>
</html>
```